Property Investor needs business card

Hi, we need a business card/logo/email footer/letterhead for a small family property investment business (based in Australia), to just give things a bit more of a professional "look".
Saying that, the property manager is in his late 30s, and is a fun, interesting guy so it doesn't have to be too "corporate" and serious.
Going with eg an 8cmx4cm card size could also make it a bit more interesting. Colour-wise - am relaxed.
Also, the property isn't so much "residential" ie houses/apartments, more "commercial" ie factories, office buildings, shops - in case that helps?
Lastly, the business name is "QHT", so you could also try to do something with those letters.
Enjoy!

```html
<!DOCTYPE html>
<html lang="en">
<head>
<meta charset="utf-8">
<title>QHT Property Investments – Stationery</title>
<link rel="stylesheet" href="https://fonts.googleapis.com/css2?family=Questrial&display=swap">
<style>
  :root {
    --bg: #f1f1f1;
    --paper: #ffffff;
    --brand-blue: #4f6fd3;
    --pale-blue: #dfe6f8;
    --ink: #4a4d55;
    --rule: #8a8d94;
    --navy-a: #26334a;
    --navy-b: #3b4a61;
    --on-navy: #c9d0dc;
  }
  * { box-sizing: border-box; margin: 0; padding: 0; }
  html, body {
    width: 1200px; height: 979px; overflow: hidden;
    background: var(--bg);
    font-family: "Questrial", "Century Gothic", sans-serif;
    color: var(--ink);
  }
  .sheet {
    position: relative; width: 1200px; height: 979px;
  }

  /* Logo lockup */
  .lockup { display: flex; align-items: center; }
  .lockup__name {
    color: var(--brand-blue);
    font-size: 34px; letter-spacing: 2px; line-height: 1;
  }
  .lockup__divider {
    width: 1px; height: 34px; background: var(--rule); margin: 0 14px;
  }
  .lockup__tagline { font-size: 13px; line-height: 1.15; color: var(--ink); }

  /* Letterhead */
  .letterhead {
    position: absolute; left: 60px; top: 48px;
    width: 622px; height: 880px;
    background: var(--paper);
    box-shadow: 0 2px 10px rgba(0,0,0,.08);
  }
  .letterhead .lockup { position: absolute; left: 64px; top: 60px; }
  .letterhead__footer {
    position: absolute; right: 64px; bottom: 0;
    display: flex; align-items: stretch;
    font-size: 10px; line-height: 1.4;
  }
  .letterhead__address { text-align: right; padding: 0 12px 30px 0; align-self: flex-end; }
  .letterhead__divider { width: 1px; background: var(--rule); margin: 0 0 30px; height: 28px; align-self: flex-end; }
  .letterhead__contact {
    width: 150px; padding: 0 12px 30px; align-self: flex-end;
    background: linear-gradient(to top, var(--pale-blue), var(--paper));
    border-bottom: 6px solid var(--brand-blue);
    height: 78px; display: flex; flex-direction: column; justify-content: flex-end;
  }
  .label { color: var(--brand-blue); }

  /* Business cards */
  .card {
    position: absolute; left: 740px;
    width: 400px; height: 240px;
    box-shadow: 0 2px 10px rgba(0,0,0,.1);
  }
  .card--front { top: 540px; background: var(--paper); padding: 42px 36px; }
  .card--back {
    top: 170px;
    background: linear-gradient(135deg, var(--navy-b), var(--navy-a));
    display: flex; align-items: center; justify-content: center;
  }
  .card--back .lockup__divider { background: var(--on-navy); }
  .card--back .lockup__tagline { color: var(--on-navy); }

  .card__body { display: flex; margin-top: 34px; }
  .card__person { width: 150px; text-align: center; }
  .card__name { color: var(--brand-blue); font-size: 12px; letter-spacing: 1px; text-transform: uppercase; }
  .card__role { font-size: 10px; margin-top: 2px; }
  .card__details { font-size: 10px; line-height: 1.45; padding-left: 20px; }
</style>
</head>
<body>
<main class="sheet">

  <section class="letterhead" aria-label="Letterhead">
    <div class="lockup">
      <span class="lockup__name">QHT</span>
      <span class="lockup__divider"></span>
      <span class="lockup__tagline">Property<br>Investments</span>
    </div>
    <footer class="letterhead__footer">
      <div class="letterhead__address">PO Box 5120<br>Ashgrove NSW 2410</div>
      <span class="letterhead__divider"></span>
      <div class="letterhead__contact">
        <span><span class="label">Phone:</span> 402 318 557</span>
        <span><span class="label">Fax:</span> 402 318 558</span>
      </div>
    </footer>
  </section>

  <section class="card card--back" aria-label="Business card back">
    <div class="lockup">
      <span class="lockup__name">QHT</span>
      <span class="lockup__divider"></span>
      <span class="lockup__tagline">Property<br>Investments</span>
    </div>
  </section>

  <section class="card card--front" aria-label="Business card front">
    <div class="lockup">
      <span class="lockup__name">QHT</span>
      <span class="lockup__divider"></span>
      <span class="lockup__tagline">Property<br>Investments</span>
    </div>
    <div class="card__body">
      <div class="card__person">
        <p class="card__name">Dana Whitfield</p>
        <p class="card__role">Managing Director</p>
      </div>
      <div class="card__details">
        Mobile: 0402 318 557<br>
        Email: dana@qhtprop.com<br>
        PO Box 5120<br>
        Ashgrove NSW 2410
      </div>
    </div>
  </section>

</main>
</body>
</html>
```